Poster design for the WILLOW WISP magic show.

We need a poster design for our magic show. This isn't your typical 'small town' magic show. Our show features world class magicians from the Velvet Lantern, in Hollywood California. The show is geared toward everyone, it is family friendly - with a little bit of an edge. We want people to see the poster and feel like they are going to have a unique and sophisticated magical experience. We also want individuals and couples to see the poster and feel like it is a show for them and not only for children.
Updates

Target Market(s)

BRT audience, family audience, the age range is anywhere from 5 - 105. Cool people.

Industry/Entity Type

Town

Requirements
Must have
• Our attached .jpg of the magician floating in the air. Poster size 24x36"
Must have text:
The 3rd Annual Albuquerque Conjuring Gala Presents (small type)
Willow Wisp (should be larger type)
November 24th - 25th
Showtimes 3:00PM & 7:30PM Saturday, 2:00PM Sunday
Tickets available at www.DorvaSeats.example For more information contact Dorva Theatre @ 505.555.0147
Nice to have
• A sort of old school/antique feeling to the poster.
Perhaps a theater marquee
Check out www.grovelumen.example - we love the feeling of this site for our poster...
Feel free to adjust the provided .jpg accordingly in regards to color/size/interaction with the rest of the poster
Should not have
• Should not have clowns, bunnies, anything that would make it feel like a 3 year old's magic themed birthday party.

```html
<!DOCTYPE html>
<html lang="en">
<head>
<meta charset="utf-8">
<title>Willow Wisp – Poster</title>
<link rel="stylesheet" href="https://fonts.googleapis.com/css2?family=Archivo+Black&family=Open+Sans:wght@700;800&display=swap">
<style>
  :root {
    --paper: #ffffff;
    --poster-red: #b42a10;
    --frame-tone: #c9483a;
    --panel-black: #0b0b0b;
    --strip-red: #a3200b;
    --sign-orange: #f7b45a;
    --sign-orange-dark: #e89a3e;
    --bulb-yellow: #fde74c;
    --ink: #1a140c;
    --gold-text: #f6e71d;
    --ticket-yellow: #fbe91d;
    --white: #ffffff;
  }
  * { margin: 0; padding: 0; box-sizing: border-box; }
  html, body { width: 1009px; height: 1200px; overflow: hidden; background: var(--paper); }
  body { position: relative; font-family: "Open Sans", Arial, sans-serif; }

  .poster {
    position: absolute; left: 100px; top: 148px; width: 801px; height: 1042px;
    background: var(--poster-red);
    box-shadow: 0 0 90px 40px rgba(200, 70, 50, 0.18);
  }
  .ornament-frame {
    position: absolute; left: 151px; top: 164px; width: 701px; height: 1011px;
    background: linear-gradient(135deg, #d8695c, var(--frame-tone) 50%, #d8695c);
    border: 3px solid #f1d7d2;
  }
  .stage-panel {
    position: absolute; left: 197px; top: 197px; width: 605px; height: 950px;
    background: radial-gradient(ellipse at 50% 40%, #1a1a1a 0%, var(--panel-black) 70%);
  }
  .marquee-header {
    position: absolute; left: 203px; top: 226px; width: 590px; height: 44px;
    background: var(--strip-red);
    color: var(--gold-text); font-weight: 700; font-size: 16.5px;
    display: flex; align-items: center; justify-content: center;
  }
  .marquee-sign { position: absolute; left: 203px; top: 269px; width: 590px; height: 170px; }
  .marquee-title {
    position: absolute; left: 203px; top: 276px; width: 590px; height: 130px;
    display: flex; align-items: center; justify-content: center;
    font-family: "Archivo Black", "Arial Black", sans-serif; color: var(--ink);
    line-height: 1; letter-spacing: -1px;
  }
  .marquee-title .small { font-size: 44px; transform: translateY(10px); }
  .marquee-title .big { font-size: 104px; }

  .show-panel {
    position: absolute; left: 206px; top: 439px; width: 587px; height: 452px;
    background: linear-gradient(to right, #f3a24a 0 10px, var(--strip-red) 10px calc(100% - 10px), #f3a24a calc(100% - 10px));
    border-radius: 0 0 10px 10px;
  }
  .show-panel::after {
    content: ""; position: absolute; left: 0; right: 0; top: 240px; bottom: 0;
    background: var(--strip-red); border-radius: 0 0 10px 10px;
  }
  .stage-photo {
    position: absolute; left: 216px; top: 439px; width: 557px; height: 340px;
    background: radial-gradient(ellipse at 50% 0%, #c84a20 0%, #8a2a12 45%, #3a120a 100%);
  }
  .show-dates {
    position: absolute; left: 206px; top: 768px; width: 587px; text-align: center;
    color: var(--white); font-weight: 800; font-size: 37px; letter-spacing: -0.3px;
  }
  .showtimes {
    position: absolute; left: 206px; top: 830px; width: 587px; text-align: center;
    color: var(--ink); font-weight: 700; font-size: 15.5px;
  }
  .ticket { position: absolute; left: 362px; top: 858px; width: 312px; height: 140px; }
  .ticket-label {
    position: absolute; left: 362px; top: 910px; width: 312px; text-align: center;
    font-weight: 800; font-size: 19px; color: var(--ink); transform: rotate(4deg);
  }
  .ticket-url {
    position: absolute; left: 197px; top: 1000px; width: 605px; text-align: center;
    color: var(--white); font-weight: 800; font-size: 32px;
  }
  .contact-bar {
    position: absolute; left: 210px; top: 1058px; width: 574px; height: 48px;
    background: var(--strip-red);
    display: flex; align-items: center; justify-content: center;
    color: var(--gold-text); font-weight: 700; font-size: 16px;
  }
</style>
</head>
<body>
  <div class="poster"></div>
  <div class="ornament-frame" role="img" aria-label="Antique red and white ornamental border pattern"></div>
  <div class="stage-panel"></div>

  <div class="marquee-header">The 3rd Annual Albuquerque Conjuring Gala Presents</div>

  <svg class="marquee-sign" viewBox="0 0 590 170" aria-hidden="true">
    <polygon points="0,0 291,-8 291,130 0,137" fill="#f7b45a"/>
    <polygon points="291,-8 590,0 590,137 291,130" fill="#f5ad50"/>
    <line x1="291" y1="-8" x2="291" y2="130" stroke="#e89a3e" stroke-width="2"/>
    <polygon points="0,137 291,130 291,170 0,170" fill="#a3200b"/>
    <polygon points="291,130 590,137 590,170 291,170" fill="#9a1e0a"/>
    <g fill="#fde74c">
      <ellipse cx="32" cy="155" rx="2.5" ry="8"/>
      <ellipse cx="80" cy="155" rx="3.5" ry="10"/>
      <ellipse cx="130" cy="155" rx="5" ry="12"/>
      <ellipse cx="185" cy="153" rx="8" ry="14"/>
      <ellipse cx="247" cy="152" rx="14" ry="17"/>
      <ellipse cx="330" cy="152" rx="14" ry="17"/>
      <ellipse cx="388" cy="153" rx="8" ry="14"/>
      <ellipse cx="435" cy="155" rx="6" ry="12"/>
      <ellipse cx="492" cy="155" rx="4" ry="10"/>
      <ellipse cx="545" cy="155" rx="2.5" ry="8"/>
    </g>
  </svg>
  <div class="marquee-title"><span class="small">Willo</span><span class="big">W</span><span class="big">W</span><span class="small">isp</span></div>

  <div class="show-panel"></div>
  <div class="stage-photo" role="img" aria-label="Photo of a magician on a red-lit stage levitating a yellow chair"></div>

  <div class="show-dates">November 24th - 25th</div>
  <div class="showtimes">Showtimes 3:00PM &amp; 7:30PM Saturday, 2:00PM Sunday</div>

  <svg class="ticket" viewBox="0 0 312 140" aria-hidden="true">
    <path transform="rotate(4 156 70)" d="M20,18 H292 Q300,18 300,26 V52 A20,20 0 0 0 300,92 V116 Q300,124 292,124 H20 Q12,124 12,116 V92 A20,20 0 0 0 12,52 V26 Q12,18 20,18 Z" fill="#fbe91d"/>
  </svg>
  <div class="ticket-label">Tickets available at</div>
  <div class="ticket-url">www.DorvaSeats.example</div>

  <div class="contact-bar">For more information contact Dorva Theatre @ 505.555.0147</div>
</body>
</html>
```